A Must Standout Business Card Design

I need A card that stands out from the rest. Possibly raised letters or Metallic card, Shiny or glossy, Looking for a more modern look or something throwback design would be nice. So i'm a open to different designs. I have a logo but not to happy with it. I will send it on a sample business card I do like.I might like you to tweak the designed card I am sending you. A new logo may be in order too. Make logo something that can be engraved on metal. I was thinking possibly KR in a box or KR mirror image or Backward E then a forward B in a circle. The name of my company is KR Works Inc. I designed an innovative hand tool to remove Valve Cores. I call the tool the Stem Pin Clasp. My tool grips and holds onto valve cores like no other tool does. Check it out at my website stempinclasp.com Maybe put a picture of the tool on the card raised or embossed or that spot gloss.
Updates
Everybody I must say have sent over some awesome designs! Every submission has been my favorite so I will be making my decision after the deadline. Nice work everyone!
Target Market(s)
Automotive people, People who wholesale refrigeration parts and equipment, People who use tools
Industry/Entity Type
Business
Contact Information for Business Card
KR Works Inc., 4172 Larkfield Rd. Unit C Elmdale OH 44990, Doug Whitlow President, 708-555-0193, Stempinclasp.com, Logo
Look and feel
Each slider illustrates characteristics of the customer's brand and the style your logo design should communicate.

```html
<!DOCTYPE html>
<html lang="en">
<head>
<meta charset="UTF-8">
<title>KR Works Inc – Business Card</title>
<link href="https://fonts.googleapis.com/css2?family=Lato:wght@400;700&display=swap" rel="stylesheet">
<style>
  :root {
    --page-bg: #e9ebee;
    --card-white: #fbfbfc;
    --card-silver: #e4e6ea;
    --brand-blue: #1f4f9c;
    --brand-blue-deep: #163f86;
    --brand-blue-light: #2d63b5;
    --stripe-pale: #8fa6c9;
    --stripe-mid: #5f7fb5;
    --rule-light: #d9dde4;
    --logo-grey: #7b818a;
    --text-white: #ffffff;
  }
  * { box-sizing: border-box; margin: 0; padding: 0; }
  html, body {
    width: 1200px; height: 1000px; overflow: hidden;
    background: var(--page-bg);
    font-family: "Lato", sans-serif;
  }
  .business-card {
    position: absolute; left: 110px; top: 220px;
    width: 980px; height: 560px;
    overflow: hidden;
    background: var(--card-white);
    box-shadow: 0 10px 30px rgba(20, 40, 80, 0.18);
  }
  .card-header {
    position: absolute; left: 0; top: 0; width: 100%; height: 207px;
    background: linear-gradient(180deg, var(--card-white) 0%, var(--card-silver) 100%);
  }
  .brand {
    position: absolute; left: 92px; top: 98px;
    display: flex; align-items: center; gap: 18px;
  }
  .brand-mark {
    width: 58px; height: 58px;
    background: var(--logo-grey);
  }
  .brand-name {
    font-size: 62px; font-weight: 400; color: var(--logo-grey);
    line-height: 1;
  }
  .card-band {
    position: absolute; left: 0; top: 207px; width: 100%; height: 353px;
    background: linear-gradient(180deg, var(--brand-blue) 0%, var(--brand-blue-light) 45%, var(--brand-blue-deep) 100%);
  }
  .band-rule {
    position: absolute; left: 0; top: 300px; width: 100%; height: 9px;
    background: var(--rule-light);
  }
  .band-stripes { position: absolute; left: 0; top: 0; }
  .person {
    position: absolute; left: 92px; top: 80px; color: var(--text-white);
  }
  .person-name { font-size: 34px; font-weight: 700; letter-spacing: 0.5px; }
  .person-title { font-size: 24px; font-weight: 400; margin-top: 4px; }
  .contacts {
    position: absolute; left: 425px; top: 72px; color: var(--text-white);
    list-style: none; font-size: 25px; line-height: 1.25;
  }
  .contact-item { display: flex; gap: 20px; margin-bottom: 14px; }
  .contact-icon { width: 34px; height: 34px; flex: none; margin-top: -2px; }
</style>
</head>
<body>
  <div class="business-card">
    <header class="card-header">
      <div class="brand">
        <span class="brand-mark"></span>
        <span class="brand-name">KR Works Inc</span>
      </div>
    </header>
    <section class="card-band">
      <svg class="band-stripes" width="980" height="353" viewBox="0 0 980 353">
        <polygon points="670,353 735,353 980,165 980,115" fill="var(--stripe-mid)"/>
        <polygon points="735,353 800,353 980,215 980,165" fill="var(--stripe-pale)"/>
      </svg>
      <div class="band-rule"></div>
      <div class="person">
        <div class="person-name">DOUG WHITLOW</div>
        <div class="person-title">President</div>
      </div>
      <ul class="contacts">
        <li class="contact-item">
          <svg class="contact-icon" viewBox="0 0 24 24"><path d="M12 3 2 12h3v8h5v-5h4v5h5v-8h3z" fill="#fff"/></svg>
          <span>4172 Larkfield Rd. Unit C Elmdale<br>OH 44990</span>
        </li>
        <li class="contact-item">
          <svg class="contact-icon" viewBox="0 0 24 24"><path d="M3 9c0-3 4-5 9-5s9 2 9 5v2h-5V9H8v2H3z M6 12h12l2 8H4z" fill="#fff"/><circle cx="12" cy="16" r="2" fill="#2d63b5"/></svg>
          <span>708-555-0193</span>
        </li>
        <li class="contact-item">
          <svg class="contact-icon" viewBox="0 0 24 24" fill="none" stroke="#fff" stroke-width="1.8"><circle cx="12" cy="12" r="9"/><ellipse cx="12" cy="12" rx="4" ry="9"/><path d="M3 12h18M5 7h14M5 17h14"/></svg>
          <span>stempinclasp.com</span>
        </li>
      </ul>
    </section>
  </div>
</body>
</html>
```